Design a poster for "Oak Bench Gathering"

I want to build the basis of an A3 poster aimed at men looking to create groups of men to provide a space outside the home where they can have discussions about how they are going as men.

The basic premise is the formation of small localised groups of men, getting together to chat and discuss their issues in much the same way as we often see women sitting in circles being honest with each other.

I don't need text/content, just a logo/icon and a couple of graphics on the poster. I will finish it in either Publisher or Photoshop so the output can be high def JPG/TIFF or PSD/PDF unlocked.

This is not just open to men, and no preference will be given to men, however, it is aimed at men as the consumers of the program, so the logo/graphics need to speak to MEN who are aware of their issues/emotions and are interested in exploring their masculinity and their interactions with community.

```html
<!DOCTYPE html>
<html lang="en">
<head>
<meta charset="utf-8">
<title>Oak Bench Gathering – Men's Group</title>
<link rel="stylesheet" href="https://fonts.googleapis.com/css2?family=Anton&family=Bebas+Neue&family=Permanent+Marker&display=block">
<style>
  :root {
    --frame: #0d0d0d;
    --violet: #7e4fcb;
    --crimson: #d7284b;
    --crimson-deep: #b81f3f;
    --ink-bar: #3a1820;
    --paper: #ffffff;
    --blush: #f8d6da;
    --tape: #ecdcb4;
    --tape-ink: #2a1a14;
    --black: #111111;
    --marker: "Permanent Marker", "Arial Black", sans-serif;
  }
  html, body {
    margin: 0;
    padding: 0;
    width: 854px;
    height: 1200px;
    overflow: hidden;
    background: var(--frame);
  }
  .poster {
    position: relative;
    width: 854px;
    height: 1200px;
    box-sizing: border-box;
    border: 10px solid var(--frame);
    background: var(--violet);
    overflow: hidden;
  }
  .abs { position: absolute; }

  .header-panel {
    left: 69px; top: 76px;
    width: 704px; height: 771px;
    background: var(--crimson);
    border-radius: 26px;
  }

  .org-name {
    left: 0; top: 104px; width: 834px;
    display: flex; align-items: center; justify-content: center; gap: 6px;
    font: 700 13px/1 Arial, Helvetica, sans-serif;
    letter-spacing: 0.5px;
    color: var(--paper);
  }
  .org-dot {
    width: 9px; height: 9px; border-radius: 50%;
    background: var(--paper);
  }
  .org-rule { top: 111px; height: 3px; background: var(--paper); }
  .org-rule.left { left: 123px; width: 180px; }
  .org-rule.right { left: 582px; width: 130px; }

  .headline { left: 110px; top: 128px; width: 630px; height: 160px; }
  .headline text {
    font-family: "Anton", sans-serif;
    font-size: 160px;
    fill: var(--paper);
  }

  .tagline-bar {
    left: 127px; top: 294px; width: 590px; height: 42px;
    background: var(--ink-bar);
    display: flex; align-items: center; justify-content: center;
    font: 16px/1 var(--marker);
    color: var(--paper);
    letter-spacing: 0.4px;
    white-space: nowrap;
  }

  .lineup-photo {
    left: 86px; top: 362px; width: 680px; height: 300px;
    background: linear-gradient(90deg, rgba(240,220,210,0.35), rgba(70,60,90,0.45) 35%, rgba(200,190,200,0.4) 60%, rgba(240,230,220,0.35));
    border-radius: 6px;
  }

  .see-you {
    left: 86px; top: 673px; width: 240px;
    text-align: center;
    font: 16px/1 Arial, Helvetica, sans-serif;
    color: var(--paper);
  }
  .day-box {
    left: 86px; top: 690px; width: 238px; height: 88px;
    background: var(--paper);
    display: flex; align-items: center; justify-content: center;
    font: 70px/1 "Anton", sans-serif;
    color: var(--black);
  }
  .divider-v { left: 331px; top: 680px; width: 2px; height: 118px; background: var(--paper); }

  .premises {
    left: 370px; top: 670px; width: 390px;
    text-align: center;
    font: 40px/1.1 "Anton", sans-serif;
    color: var(--blush);
    white-space: nowrap;
  }
  .address {
    left: 370px; top: 722px; width: 390px;
    text-align: center;
    font: 15px/1 Arial, Helvetica, sans-serif;
    color: var(--paper);
  }
  .divider-h { left: 346px; top: 750px; width: 418px; height: 2px; background: var(--paper); }

  .from-tag { left: 346px; top: 764px; width: 180px; height: 32px; }
  .from-tag text {
    font-family: var(--marker);
    font-size: 16px;
    fill: var(--black);
  }
  .hours {
    left: 526px; top: 762px; width: 240px;
    text-align: center;
    font: 36px/1 "Bebas Neue", sans-serif;
    color: var(--blush);
    transform: skewX(-8deg);
    white-space: nowrap;
  }

  .promise-bar {
    left: 63px; top: 896px; width: 706px; height: 44px;
    background: var(--crimson-deep);
    display: flex; align-items: center; justify-content: center;
    font: 16px/1 var(--marker);
    color: var(--paper);
    letter-spacing: 0.3px;
    white-space: nowrap;
  }

  .welcome-tape {
    left: 205px; top: 1038px; width: 372px; height: 68px;
    background: var(--tape);
    transform: rotate(-8deg);
    display: flex; align-items: center; justify-content: center;
    font: 34px/1 var(--marker);
    color: var(--tape-ink);
    box-shadow: 0 3px 8px rgba(0,0,0,0.25);
  }

  .greeter-photo {
    left: 578px; top: 978px; width: 134px; height: 202px;
    background: linear-gradient(180deg, rgba(240,200,180,0.55), rgba(200,170,160,0.6) 45%, rgba(190,110,90,0.6));
    border-radius: 60px 60px 4px 4px;
  }
</style>
</head>
<body>
<main class="poster">
  <div class="abs header-panel"></div>

  <div class="abs org-rule left"></div>
  <div class="abs org-name"><span class="org-dot"></span>OAK BENCH GATHERING</div>
  <div class="abs org-rule right"></div>

  <svg class="abs headline" viewBox="0 0 630 160" aria-label="Men's Group">
    <text x="0" y="150" textLength="630" lengthAdjust="spacingAndGlyphs">MEN’S GROUP</text>
  </svg>

  <div class="abs tagline-bar">WEEKLY SUPPORT MEETINGS FOR MEN OF ALL AGES</div>

  <div class="abs lineup-photo" role="img" aria-label="Photo of seven men of different ages and styles standing side by side"></div>

  <div class="abs see-you">SEE YOU EVERY</div>
  <div class="abs day-box">MONDAY</div>
  <div class="abs divider-v"></div>

  <div class="abs premises">PREMISES GOES HERE</div>
  <div class="abs address">ADDRESS GOES HERE</div>
  <div class="abs divider-h"></div>

  <svg class="abs from-tag" viewBox="0 0 180 32">
    <polygon points="0,0 160,0 180,16 160,32 0,32 10,16" fill="#ffffff"/>
    <text x="56" y="22">FROM</text>
  </svg>
  <div class="abs hours">6.30PM TO 8.30PM</div>

  <div class="abs promise-bar">MAKE NEW CONNECTIONS IN A NON-JUDGEMENTAL SUPPORTIVE PLACE</div>

  <div class="abs welcome-tape">ALL WELCOME</div>
  <div class="abs greeter-photo" role="img" aria-label="Photo of a smiling older man giving a thumbs up"></div>
</main>
</body>
</html>
```